Business Card for premium dental clinic

We are a premium dental clinic based in Brasov, Romania with more than 15 year on the market, providing quality dental treatment made by a team of more specialized dentists, working with modern equipment as a solution to beautiful and healthy teeth.

Our current logo for the clinic use 2 square with colors black and gold - dr Corbescu - studio, using family fonts Bodoni, Myriad Pro and Segoe Print.
Depending on the printing we used some gold CMYK background or gold foil picture background or a gold gradient.
We want a business card:
- eye catching business card
- distinguished business card
- premium design
- to keep the color scheme of black and gold
- to attract the customers to spent time reading the information
- modern concept

```html
<!DOCTYPE html>
<html lang="en">
<head>
<meta charset="utf-8">
<title>Lumen Dental Clinic – Business Card</title>
<link rel="stylesheet" href="https://fonts.googleapis.com/css2?family=Fira+Sans+Condensed:wght@300;400&family=Montserrat:wght@400;500&display=swap">
<style>
  :root {
    --stage: #2b2b2b;
    --card: #0b0b0b;
    --ink: #000000;
    --white: #ffffff;
    --paper: #f5f5f5;
    --gold: #f2c230;
    --gold-light: #ffe27a;
    --gold-deep: #b8860b;
    --arc: #2f2f2f;
    --arc-fill: #141414;
  }
  * { box-sizing: border-box; margin: 0; padding: 0; }
  html, body { width: 1200px; height: 900px; overflow: hidden; }
  body { background: var(--stage); position: relative; font-family: "Montserrat", Arial, sans-serif; }

  .card {
    position: absolute;
    left: 280px;
    width: 640px;
    height: 366px;
    background: var(--card);
    overflow: hidden;
  }
  .card--front { top: 50px; }
  .card--back { top: 484px; }

  /* Front */
  .front-frame {
    position: absolute;
    left: 90px; top: 60px;
    width: 460px; height: 230px;
    border: 2px solid var(--white);
    display: flex;
  }
  .gold-foil {
    width: 50%;
    height: 100%;
    background: radial-gradient(ellipse at 35% 40%, var(--gold-light) 0%, var(--gold) 45%, var(--gold-deep) 100%);
  }
  .front-brand {
    width: 50%;
    height: 100%;
    background: var(--ink);
    position: relative;
  }
  .name-band {
    position: absolute;
    left: 40px; top: 92px;
    width: 210px; height: 64px;
    background: var(--paper);
    display: flex; align-items: flex-end; justify-content: center;
    padding-bottom: 10px;
    color: var(--ink);
  }
  .doctor-name { font-family: "Fira Sans Condensed", Arial, sans-serif; font-weight: 300; white-space: nowrap; line-height: 1; }
  .doctor-name .title { font-size: 22px; }
  .doctor-name .surname { font-size: 38px; }

  .clinic-name {
    font-family: "Montserrat", Arial, sans-serif;
    font-weight: 400;
    color: var(--white);
    line-height: 1.1;
  }
  .front-brand .clinic-name {
    position: absolute;
    left: 32px; top: 62px;
    font-size: 36px;
  }
  .front-brand .clinic-name small { display: block; font-size: 17px; text-align: right; margin-top: 18px; }
  .brand-mark { position: absolute; width: 14px; height: 14px; background: var(--gold); }
  .front-brand .brand-mark { left: 32px; top: 44px; }

  .front-web {
    position: absolute;
    left: 0; right: 0; top: 306px;
    text-align: center;
    font-size: 17px;
    letter-spacing: 0.5px;
    color: var(--white);
  }
  .front-web .accent { color: var(--gold); font-weight: 500; }

  /* Back */
  .back-arc { position: absolute; inset: 0; }
  .back-brand {
    position: absolute;
    left: 0; right: 0; top: 52px;
    display: flex; align-items: center; justify-content: center; gap: 14px;
  }
  .back-brand .brand-mark { position: static; width: 18px; height: 18px; }
  .back-brand .clinic-name { font-size: 30px; }
  .back-brand .clinic-name small { font-size: 15px; margin-left: 6px; }

  .name-box {
    position: absolute;
    left: 40px; top: 220px;
    width: 200px; height: 64px;
    border: 1px solid var(--gold);
    display: flex; align-items: center; justify-content: center;
    color: var(--white);
  }
  .divider {
    position: absolute;
    left: 266px; top: 190px;
    width: 1px; height: 110px;
    background: #8a8a8a;
  }
  .contact-list {
    position: absolute;
    left: 290px; top: 192px;
    list-style: none;
    color: var(--white);
    font-size: 17px;
    letter-spacing: 0.3px;
  }
  .contact-list li { display: flex; align-items: center; gap: 14px; height: 34px; }
  .contact-list svg { width: 18px; height: 18px; flex: none; }
</style>
</head>
<body>

<section class="card card--front">
  <div class="front-frame">
    <div class="gold-foil" role="img" aria-label="Gold foil texture background"></div>
    <div class="front-brand">
      <span class="brand-mark"></span>
      <p class="clinic-name">lumen<small>dental clinic</small></p>
    </div>
    <div class="name-band">
      <p class="doctor-name"><span class="title">dr.</span><span class="surname">Corbescu</span></p>
    </div>
  </div>
  <p class="front-web">info.<span class="accent">lumendental</span>.com</p>
</section>

<section class="card card--back">
  <svg class="back-arc" width="640" height="366" viewBox="0 0 640 366" aria-hidden="true">
    <ellipse cx="690" cy="560" rx="600" ry="420" fill="var(--arc-fill)" stroke="var(--arc)" stroke-width="14"/>
  </svg>

  <div class="back-brand">
    <span class="brand-mark"></span>
    <p class="clinic-name">lumen<small>dental clinic</small></p>
  </div>

  <div class="name-box">
    <p class="doctor-name"><span class="title">dr.</span><span class="surname">Corbescu</span></p>
  </div>

  <span class="divider"></span>

  <ul class="contact-list">
    <li>
      <svg viewBox="0 0 24 24" fill="none" stroke="var(--gold)" stroke-width="2" stroke-linecap="round" stroke-linejoin="round"><path d="M5 3h4l2 5-2.5 1.5a11 11 0 0 0 6 6L16 13l5 2v4a2 2 0 0 1-2 2A16 16 0 0 1 3 5a2 2 0 0 1 2-2z"/></svg>
      +00 000 555 0142
    </li>
    <li>
      <svg viewBox="0 0 24 24" fill="none" stroke="var(--gold)" stroke-width="2" stroke-linecap="round"><rect x="7" y="2" width="10" height="20" rx="2"/><path d="M11 18h2"/></svg>
      +00 000 555 0142
    </li>
    <li>
      <svg viewBox="0 0 24 24" fill="none" stroke="var(--gold)" stroke-width="2" stroke-linejoin="round"><rect x="3" y="5" width="18" height="14"/><path d="M3 5l9 7 9-7"/></svg>
      info@lumendental.com
    </li>
  </ul>
</section>

</body>
</html>
```